Business Card Design

Recruitment Company. Want to keep the logo and the green colour

Industry/Entity Type

Business

Contact Information for Business Card

Hi,

1.)
MARTIN COLLARD
Director
Level 4, 238 Finch Terrace
Brisbane QLD 4000
M 0412 604 337
E martin@paceltalent.com.au
www.paceltalent.com.au

2.)
TOM WHITFORD
Director
Level 4, 238 Finch Terrace
Brisbane QLD 4000
M 0419 572 641
E tom@paceltalent.com.au

Want something different and eye catching, happy for you guys to use your design flare to work some magic with these.

Many Thanks
Tom

```html
<!DOCTYPE html>
<html lang="en">
<head>
<meta charset="utf-8">
<title>Pacel Talent – Business Cards</title>
<link rel="stylesheet" href="https://fonts.googleapis.com/css2?family=Open+Sans:wght@400;600;700&display=swap">
<style>
  :root {
    --page-bg: #f4f4f3;
    --paper: #e8e7e4;
    --ink: #1d1d1b;
    --ink-soft: #4a4a48;
    --brand-green: #6cbf4f;
    --band-green: #5db44a;
    --band-lime: #b3c23c;
    --edge-yellow: #d8d23a;
    --card-w: 540px;
    --card-h: 309px;
  }
  * { box-sizing: border-box; margin: 0; padding: 0; }
  html, body {
    width: 1200px;
    height: 900px;
    overflow: hidden;
    background: var(--page-bg);
    font-family: "Open Sans", Arial, sans-serif;
    color: var(--ink);
  }
  .card-sheet {
    width: 1200px;
    height: 900px;
    display: flex;
    align-items: center;
    justify-content: center;
    gap: 40px;
  }
  .business-card {
    position: relative;
    width: var(--card-w);
    height: var(--card-h);
    background: var(--paper);
    overflow: hidden;
    box-shadow: 0 6px 18px rgba(0,0,0,0.12);
  }
  .business-card--lime { --band: var(--band-lime); }
  .business-card--green { --band: var(--band-green); }
  .card-band {
    position: absolute;
    inset: 0;
    width: 100%;
    height: 100%;
  }
  .card-band__fill { fill: var(--band); }
  .card-band__edge { fill: none; stroke: var(--edge-yellow); stroke-width: 3; }
  .brand {
    position: absolute;
    left: 34px;
    top: 34px;
    display: flex;
    align-items: center;
    gap: 10px;
  }
  .brand__dot {
    width: 16px;
    height: 16px;
    border-radius: 50%;
    background: var(--brand-green);
  }
  .brand__name {
    font-size: 34px;
    font-weight: 600;
    color: var(--brand-green);
    letter-spacing: -0.5px;
    line-height: 1;
  }
  .holder {
    position: absolute;
    left: 300px;
    top: 88px;
  }
  .holder__name {
    font-size: 24px;
    font-weight: 700;
    letter-spacing: 0.5px;
    line-height: 1.1;
  }
  .holder__title {
    font-size: 13px;
    color: var(--ink-soft);
  }
  .contact {
    position: absolute;
    left: 34px;
    top: 152px;
    font-size: 14px;
    line-height: 1.45;
    list-style: none;
  }
  .contact__address { margin-bottom: 4px; }
  .contact__row {
    display: flex;
    align-items: center;
    gap: 10px;
  }
  .contact__icon { width: 12px; height: 12px; flex: none; }
  .contact__icon * { fill: var(--ink); }
  .contact__rule {
    width: 250px;
    height: 1px;
    background: var(--ink);
    margin: 4px 0 4px 22px;
  }
</style>
</head>
<body>
<main class="card-sheet">

  <article class="business-card business-card--lime">
    <svg class="card-band" viewBox="0 0 540 309" preserveAspectRatio="none" aria-hidden="true">
      <path class="card-band__fill" d="M0,112 C170,104 300,168 540,178 L540,309 L0,309 Z"/>
      <path class="card-band__edge" d="M0,112 C170,104 300,168 540,178"/>
    </svg>
    <div class="brand">
      <span class="brand__dot"></span>
      <span class="brand__name">Pacel Talent</span>
    </div>
    <header class="holder">
      <h2 class="holder__name">MARTIN COLLARD</h2>
      <p class="holder__title">Director Level 4</p>
    </header>
    <ul class="contact">
      <li class="contact__address">238 Finch Terrace Brisbane<br>QLD 4000 M</li>
      <li class="contact__row">
        <svg class="contact__icon" viewBox="0 0 12 12"><circle cx="6" cy="6" r="6"/></svg>
        <span>0412 604 337</span>
      </li>
      <li class="contact__rule"></li>
      <li class="contact__row">
        <svg class="contact__icon" viewBox="0 0 12 12"><rect x="0" y="2" width="12" height="8"/></svg>
        <span>martin@paceltalent.com.au</span>
      </li>
      <li class="contact__row">
        <svg class="contact__icon" viewBox="0 0 12 12"><circle cx="6" cy="6" r="6"/></svg>
        <span>www.paceltalent.com.au</span>
      </li>
    </ul>
  </article>

  <article class="business-card business-card--green">
    <svg class="card-band" viewBox="0 0 540 309" preserveAspectRatio="none" aria-hidden="true">
      <path class="card-band__fill" d="M0,112 C170,104 300,168 540,178 L540,309 L0,309 Z"/>
      <path class="card-band__edge" d="M0,112 C170,104 300,168 540,178"/>
    </svg>
    <div class="brand">
      <span class="brand__dot"></span>
      <span class="brand__name">Pacel Talent</span>
    </div>
    <header class="holder">
      <h2 class="holder__name">TOM WHITFORD</h2>
      <p class="holder__title">Director Level 4</p>
    </header>
    <ul class="contact">
      <li class="contact__address">238 Finch Terrace Brisbane<br>QLD 4000 M</li>
      <li class="contact__row">
        <svg class="contact__icon" viewBox="0 0 12 12"><circle cx="6" cy="6" r="6"/></svg>
        <span>0419 572 641</span>
      </li>
      <li class="contact__rule"></li>
      <li class="contact__row">
        <svg class="contact__icon" viewBox="0 0 12 12"><rect x="0" y="2" width="12" height="8"/></svg>
        <span>tom@paceltalent.com.au</span>
      </li>
      <li class="contact__row">
        <svg class="contact__icon" viewBox="0 0 12 12"><circle cx="6" cy="6" r="6"/></svg>
        <span>www.paceltalent.com.au</span>
      </li>
    </ul>
  </article>

</main>
</body>
</html>
```